A3 Poster for The Melrow Fund Global Winter Medical Appeal

We require an A3 poster for The Melrow Fund Winter Medical Appeal for Syria and Gaza (should also be able to be converted to A5 for leaflets). The Melrow Fund is a UK registered charity specialising in International Medical Aid. The poster needs to be EYE catching and convey our professional medicla ethos
A3 Lanscape
1) At the top - Logo - like Pevious Poster deisgn
2) WINTER MEDICAL APPEAL (make MEDICAL stand out - maybe put in red or make larger)
INTERNATIONAL MEDICAL AID

SYRIA MEDICAL PACKS
PACK 1 £20
(Airway equipment, surgical pack, dressing pack)
PACK 2 £50
(Pack 1 + Blood stopper, specialised dressings)
PACK 3 £100
(Pack 1+2 + Chest drain, IV access, drugs)
To donate by TEXT
Text KTVB07 £5 to 81482

Along the above to the right have:

GAZA DISABLED CHILDREN
Spectacles £20
Wheelchair £130
Hearing Aid £300
To donate by TEXT
Text PLOM07 £5 to 81482

www.melrow-fund.org
Updates

Uploaded a photo - Snow Syria - if feasible could you put this behind the title "WINTER MEDICAL APPEAL"

At the very bottom of the poster can you add text "The Melrow Fund Global - Registered Charity No. 1187926"
Many thanks

Target Market(s)

Donors - when you look at the poster it should make you contemplate helping the recipients and donating to the appeal

Industry/Entity Type

Charity

Font styles to use
Sans Serif

Requirements
Must have
• Our Logo preferably at the top and our website at the botton
Facebook, Twitter, You Tube icons at the bottom
Our wesbite at the bottom
On the Previous Poster file we like the way the logo comes down from the top but this poster is too dull for this appeal
Do not show women in the poster - just men and kids
ADD Image behind SYRIA text - showing a hospital theatre
ADD Images behind GAZA CHILDREN text - injured children in Gaza
Nice to have
• Have attached a Snow Image of Syria would be nice to have incorporated near top of poster where it says "WINTER MEDICAL APPEAL"

```html
<!DOCTYPE html>
<html lang="en">
<head>
<meta charset="utf-8">
<title>The Melrow Fund Global – Winter Medical Appeal</title>
<link rel="stylesheet" href="https://fonts.googleapis.com/css2?family=Anton&family=Lato:wght@400;700&family=Cinzel:wght@400&display=swap">
<style>
  :root {
    --paper: #ffffff;
    --ink: #000000;
    --frost: #e4eaf2;
    --ice-light: #dfe7f1;
    --ice-mid: #9fb2c9;
    --ice-dark: #5f7590;
    --accent-blue: #8db0d8;
    --photo-top: #6f87a4;
    --photo-mid: #4a6079;
    --photo-low: #2c3b4f;
    --tile: #3a4657;
  }
  html, body {
    margin: 0;
    padding: 0;
    width: 1200px;
    height: 860px;
    overflow: hidden;
    background: var(--paper);
  }
  .poster {
    position: relative;
    width: 1200px;
    height: 860px;
    background: var(--paper);
    font-family: "Lato", sans-serif;
  }
  .poster__board {
    position: absolute;
    left: 28px;
    top: 25px;
    width: 1140px;
    height: 807px;
    background: var(--ink);
  }
  .site-line {
    position: absolute;
    top: 62px;
    left: 185px;
    width: 825px;
    display: flex;
    align-items: center;
    gap: 18px;
    color: var(--frost);
    font-size: 20px;
    letter-spacing: 2px;
  }
  .site-line::before,
  .site-line::after {
    content: "";
    flex: 1;
    height: 2px;
    background: var(--frost);
  }
  .headline {
    position: absolute;
    margin: 0;
    font-family: "Anton", sans-serif;
    font-weight: 400;
    line-height: 1;
    text-transform: uppercase;
    background: linear-gradient(180deg, var(--ice-light) 0%, var(--ice-mid) 55%, var(--ice-dark) 100%);
    -webkit-background-clip: text;
    background-clip: text;
    color: transparent;
  }
  .headline--winter { left: 176px; top: 157px; font-size: 90px; letter-spacing: 1px; transform: scaleY(0.9); transform-origin: left top; }
  .headline--medical { left: 460px; top: 104px; font-size: 160px; letter-spacing: 1px; transform: scaleY(0.88); transform-origin: left top; }
  .headline--appeal { left: 750px; top: 245px; font-size: 122px; letter-spacing: 18px; transform: scaleY(0.86); transform-origin: left top; }
  .hero-photo {
    position: absolute;
    left: 43px;
    top: 262px;
    width: 675px;
    height: 435px;
    background: linear-gradient(180deg, var(--photo-top) 0%, var(--photo-mid) 45%, var(--photo-low) 100%);
  }
  .appeal-details {
    position: absolute;
    left: 745px;
    top: 375px;
    width: 410px;
    color: var(--accent-blue);
  }
  .appeal-details__lead {
    margin: 0 0 16px;
    color: var(--paper);
    font-size: 21px;
    letter-spacing: 2.2px;
  }
  .appeal-details__group-title {
    margin: 0 0 6px;
    font-size: 19px;
    font-weight: 700;
    letter-spacing: 1.4px;
  }
  .pack-list, .item-list { list-style: none; margin: 0; padding: 0; }
  .pack-list__name {
    display: block;
    font-size: 14px;
    font-weight: 700;
    letter-spacing: 1px;
    line-height: 18px;
  }
  .pack-list__contents,
  .donate-line {
    display: block;
    font-size: 12px;
    letter-spacing: 1px;
    line-height: 16px;
    text-transform: uppercase;
  }
  .gaza-group { margin-top: 36px; }
  .item-list li {
    font-size: 14px;
    letter-spacing: 1px;
    line-height: 19px;
    text-transform: uppercase;
  }
  .gaza-group .donate-line { font-size: 14px; line-height: 19px; }
  .social-row {
    position: absolute;
    left: 45px;
    top: 712px;
    display: flex;
    gap: 14px;
  }
  .social-row__tile { width: 45px; height: 45px; background: var(--tile); }
  .brand-badge {
    position: absolute;
    left: 222px;
    top: 712px;
    width: 140px;
    height: 45px;
    background: var(--paper);
    display: flex;
    align-items: center;
    gap: 6px;
    padding: 0 6px;
    box-sizing: border-box;
  }
  .brand-badge__dot { width: 22px; height: 22px; border-radius: 50%; background: var(--ice-dark); flex: none; }
  .brand-badge__name {
    font-size: 12px;
    font-weight: 700;
    color: var(--ice-dark);
    text-transform: uppercase;
    letter-spacing: 0.5px;
  }
  .footer-line {
    position: absolute;
    left: 28px;
    width: 1140px;
    top: 791px;
    margin: 0;
    text-align: center;
    font-family: "Cinzel", serif;
    font-size: 19px;
    letter-spacing: 2.5px;
    color: var(--frost);
  }
</style>
</head>
<body>
<main class="poster">
  <div class="poster__board"></div>

  <p class="site-line">www.melrow-fund.org</p>

  <h1 class="headline headline--winter">Winter</h1>
  <p class="headline headline--medical">Medical</p>
  <p class="headline headline--appeal">Appeal</p>

  <div class="hero-photo" role="img" aria-label="Snow-covered ruined city street in Syria with a child's face blended into the scene"></div>

  <section class="appeal-details">
    <p class="appeal-details__lead">INTERNATIONAL MEDICAL AID</p>

    <div class="syria-group">
      <h2 class="appeal-details__group-title">SYRIA MEDICAL PACKS</h2>
      <ul class="pack-list">
        <li><span class="pack-list__name">PACK 1 £20</span><span class="pack-list__contents">(Airway equipment, surgical pack, dressing pack)</span></li>
        <li><span class="pack-list__name">PACK 2 £50</span><span class="pack-list__contents">(Pack 1 + blood stopper, specialised dressings)</span></li>
        <li><span class="pack-list__name">PACK 3 £100</span><span class="pack-list__contents">(Pack 1+2 + chest drain, IV access, drugs)</span></li>
      </ul>
      <span class="donate-line">To donate: KTVB07 £5 to 81482</span>
    </div>

    <div class="gaza-group">
      <h2 class="appeal-details__group-title">GAZA DISABLED CHILDREN</h2>
      <ul class="item-list">
        <li>Spectacles £20</li>
        <li>Wheelchair £130</li>
        <li>Hearing aid £300</li>
      </ul>
      <span class="donate-line">To donate: PLOM07 £5 to 81482</span>
    </div>
  </section>

  <div class="social-row" aria-label="Social media links">
    <span class="social-row__tile"></span>
    <span class="social-row__tile"></span>
    <span class="social-row__tile"></span>
  </div>

  <div class="brand-badge">
    <span class="brand-badge__dot"></span>
    <span class="brand-badge__name">The Melrow Fund</span>
  </div>

  <p class="footer-line">The Melrow Fund Global - Registered Charity No. 1187926</p>
</main>
</body>
</html>
```